Web Design for an Online Dating Web Site

We need an uncoded web design for a new online dating web site called zMatchy.net. Simplicity and boldness are the key factors in the successful design.
Please look at the requirements document attached for details.
Updates
Dear all,
Please AVOID USING A PICTURE OF A HAPPY COUPLE ON THE HOME PAGE of the site. We highly want to move away from this space as it makes our web site just like another dating web site.
We like something simple with web 2.0 look and feel. The examples in the Requirements Document are exactly the design we are after.
Regards
Tarn
Industry/Entity Type
Dating
Look and feel
Each slider illustrates characteristics of the customer's brand and the style your logo design should communicate.

```html
<!DOCTYPE html>
<html lang="en">
<head>
<meta charset="utf-8">
<title>zMatchy.net</title>
<link rel="stylesheet" href="https://fonts.googleapis.com/css2?family=Arimo:wght@400;700&family=Comfortaa:wght@400;700&display=swap">
<style>
  :root {
    --pink: #e0348a;
    --pink-dark: #b8186c;
    --pink-soft: #f07ab4;
    --page-bg: #fdeef5;
    --canvas-bg: #ffffff;
    --slate: #577884;
    --slate-dark: #42606b;
    --grey-text: #8a8a8a;
    --grey-btn: #7b7b7b;
    --field-border: #9a9a9a;
    --footer-top: #f4f4f4;
    --footer-bottom: #dcdcdc;
    --panel-top: #dfeaf3;
    --panel-bottom: #ffffff;
    --like: #f4c21f;
    --video-dark: #2e2e2e;
    --video-light: #8c8c8c;
  }
  * { box-sizing: border-box; margin: 0; padding: 0; }
  html, body {
    width: 1200px; height: 900px; overflow: hidden;
    background: var(--canvas-bg);
    font-family: "Arimo", Arial, sans-serif;
  }
  .page {
    position: absolute; left: 174px; top: 115px;
    width: 851px; height: 671px;
    background: var(--page-bg);
  }
  .page > * { position: absolute; }

  /* brand */
  .brand { left: 0; width: 851px; top: 8px; text-align: center; }
  .brand-name {
    font-family: "Comfortaa", sans-serif; font-weight: 700;
    font-size: 62px; line-height: 1; color: var(--pink); letter-spacing: -1px;
  }
  .brand-url {
    font-family: "Comfortaa", sans-serif; font-size: 12px; color: var(--grey-text);
    margin-top: 2px;
  }

  /* navigation */
  .main-nav { top: 99px; left: 0; width: 851px; height: 24px; }
  .nav-item {
    position: absolute; top: 0; height: 24px;
    background: linear-gradient(var(--slate), var(--slate-dark));
    color: #fff; font-family: "Comfortaa", sans-serif; font-size: 13px;
    line-height: 24px; text-align: center; border-radius: 3px;
  }

  /* login */
  .login { left: 0; top: 132px; width: 205px; height: 160px; }
  .login-row { position: absolute; left: 0; width: 205px; height: 20px; }
  .login-label {
    position: absolute; right: 134px; top: 4px;
    font-size: 10px; color: var(--pink);
  }
  .login-field {
    position: absolute; left: 73px; top: 0; width: 128px; height: 19px;
    border: 1px solid var(--pink-soft); background: #fff; border-radius: 2px;
  }
  .login-btn {
    position: absolute; left: 156px; top: 55px; width: 42px; height: 14px;
    background: var(--pink); color: #fff; font-size: 9px; line-height: 14px;
    text-align: center; border-radius: 2px;
  }
  .login-or {
    position: absolute; left: 176px; top: 78px; font-size: 9px; font-weight: 700; color: #555;
  }
  .alt-login {
    position: absolute; right: 6px; font-size: 11px; font-weight: 700;
    display: flex; gap: 8px; align-items: center;
  }
  .alt-login span { display: flex; align-items: center; gap: 3px; }
  .alt-login i { display: inline-block; width: 9px; height: 9px; }
  .login-more { position: absolute; right: 8px; top: 136px; font-size: 13px; color: var(--pink); }

  /* slider */
  .slider { left: 209px; top: 136px; width: 442px; height: 205px; }

  /* recent posts */
  .recent-posts {
    left: 660px; top: 136px; width: 172px; height: 341px;
    background: linear-gradient(var(--panel-top), var(--panel-bottom));
  }
  .recent-posts h2 {
    font-size: 13px; font-weight: 400; color: #6c7f8c; text-align: center; margin-top: 8px;
  }

  .signup-cta {
    left: 253px; top: 398px; width: 77px; height: 31px;
    background: linear-gradient(var(--pink-soft), var(--pink-dark));
    border: 2px solid #fff; border-radius: 4px; box-shadow: 0 0 0 1px #c5c5c5;
    color: #fff; font-family: "Comfortaa", sans-serif; font-size: 14px;
    line-height: 27px; text-align: center;
  }
  .video {
    left: 341px; top: 381px; width: 158px; height: 95px;
    background: linear-gradient(var(--video-light), var(--video-dark) 55%);
    border: 3px solid #9c9c9c; border-radius: 3px;
  }
  .video-play { left: 506px; top: 395px; width: 35px; height: 35px; }

  /* footer */
  .site-footer {
    left: 18px; top: 488px; width: 836px; height: 183px;
    background: linear-gradient(var(--footer-top), var(--footer-bottom));
    border-radius: 10px 10px 0 0;
  }
  .site-footer > * { position: absolute; }
  .footer-brand {
    left: 14px; top: 56px; font-family: "Comfortaa", sans-serif; font-weight: 700;
    font-size: 28px; color: var(--pink);
  }
  .footer-btn {
    top: 14px; height: 26px; background: var(--grey-btn); color: #fff;
    font-size: 11px; font-weight: 700; line-height: 26px; text-align: center; border-radius: 4px;
  }
  .footer-links {
    left: 155px; top: 46px; width: 116px; list-style: none; text-align: center;
    font-size: 11px; color: #777; line-height: 19px;
  }
  .form-label { font-size: 10px; color: #666; }
  .form-field { background: #fff; border: 1px solid var(--field-border); border-radius: 2px; }
  .post-btn {
    left: 576px; top: 152px; width: 40px; height: 17px; background: #e9e9e9;
    border: 1px solid var(--field-border); font-size: 10px; line-height: 15px; text-align: center;
  }
  .share {
    left: 648px; top: 14px; width: 180px; display: grid;
    grid-template-columns: repeat(3, 58px); row-gap: 16px;
    font-size: 9px; font-weight: 700; color: #4a6f9b;
  }
  .share span { display: flex; align-items: center; gap: 3px; }
  .share i { width: 9px; height: 9px; background: #4a6f9b; display: inline-block; }
  .like-btn {
    left: 648px; top: 90px; width: 40px; height: 22px; background: var(--like);
    color: #fff; font-size: 11px; font-weight: 700; line-height: 22px; text-align: center; border-radius: 2px;
  }
  .like-box {
    left: 696px; top: 90px; width: 90px; height: 22px; background: #fff;
    border: 1px solid var(--like); border-radius: 2px;
  }
</style>
</head>
<body>
<div class="page">
  <header class="brand">
    <div class="brand-name">zMatchy</div>
    <div class="brand-url">zMatchy.net</div>
  </header>

  <nav class="main-nav">
    <span class="nav-item" style="left:253px;width:68px">why</span>
    <span class="nav-item" style="left:328px;width:112px">how it works</span>
    <span class="nav-item" style="left:448px;width:70px">sign up</span>
    <span class="nav-item" style="left:523px;width:88px">our blog</span>
  </nav>

  <section class="login">
    <div class="login-row" style="top:4px"><span class="login-label">user name</span><span class="login-field"></span></div>
    <div class="login-row" style="top:26px"><span class="login-label">password</span><span class="login-field"></span></div>
    <span class="login-btn">login</span>
    <span class="login-or">OR</span>
    <div class="alt-login" style="top:94px;color:#3b5b98">
      <span><i style="background:#3b5b98"></i>FriendLoop</span>
      <span style="color:#2a4a7a">MyCorner</span>
    </div>
    <div class="alt-login" style="top:117px">
      <span style="color:#c7392b">PostMail</span>
      <span style="color:#6b1fa0">Yodel</span>
    </div>
    <span class="login-more">more</span>
  </section>

  <svg class="slider" viewBox="0 0 442 205" aria-label="Feature slider">
    <defs>
      <linearGradient id="slideFill" x1="0" y1="0" x2="0" y2="1">
        <stop offset="0" stop-color="#d24392"/>
        <stop offset="1" stop-color="#a3165f"/>
      </linearGradient>
    </defs>
    <rect width="442" height="205" rx="6" fill="url(#slideFill)"/>
    <path d="M0 110 C90 70 170 150 270 115 C340 92 400 100 442 120 L442 205 L0 205 Z" fill="#b11f6c" opacity="0.7"/>
    <path d="M0 110 C90 70 170 150 270 115 C340 92 400 100 442 120" fill="none" stroke="#e585b6" stroke-width="1.5"/>
    <rect x="0" y="84" width="22" height="30" fill="#d7d7d7" opacity="0.8"/>
    <path d="M15 90 L6 99 L15 108" fill="none" stroke="#9a9a9a" stroke-width="3"/>
    <rect x="420" y="84" width="22" height="30" fill="#d7d7d7" opacity="0.8"/>
    <path d="M427 90 L436 99 L427 108" fill="none" stroke="#9a9a9a" stroke-width="3"/>
    <g fill="#ffffff">
      <circle cx="186" cy="190" r="5"/><circle cx="203" cy="190" r="5"/>
      <circle cx="220" cy="190" r="5"/><circle cx="237" cy="190" r="5"/>
      <circle cx="254" cy="190" r="5"/>
    </g>
  </svg>

  <aside class="recent-posts"><h2>Recent Posts</h2></aside>

  <span class="signup-cta">sign up</span>
  <div class="video" role="img" aria-label="Introductory video player"></div>
  <svg class="video-play" viewBox="0 0 35 35" aria-label="Play video">
    <circle cx="17.5" cy="17.5" r="16" fill="#2f2f2f" stroke="#bbb" stroke-width="2"/>
    <path d="M13 10 L25 17.5 L13 25 Z" fill="#fff"/>
  </svg>

  <footer class="site-footer">
    <span class="footer-brand">zMatchy</span>
    <span class="footer-btn" style="left:167px;width:90px">Read More</span>
    <ul class="footer-links">
      <li>Why zMatchy</li><li>How it works</li><li>Sign Up</li><li>Login</li><li>About Us</li>
    </ul>
    <span class="footer-btn" style="left:275px;width:88px">Let's Talk</span>
    <span class="form-label" style="left:275px;top:47px">Name</span>
    <span class="form-field" style="left:275px;top:62px;width:165px;height:24px"></span>
    <span class="form-label" style="left:275px;top:96px">E-mail</span>
    <span class="form-field" style="left:275px;top:110px;width:165px;height:24px"></span>
    <span class="form-label" style="left:453px;top:47px">Comment</span>
    <span class="form-field" style="left:453px;top:62px;width:163px;height:84px"></span>
    <span class="post-btn">Post</span>
    <div class="share">
      <span><i></i>LinkUp</span>
      <span><i></i>Chirper</span>
      <span><i></i>FriendLoop</span>
      <span><i></i>Wanderly</span>
      <span><i></i>FeedPal</span>
    </div>
    <span class="like-btn">Like</span>
    <span class="like-box"></span>
  </footer>
</div>
</body>
</html>
```